Halvorsen Basin Holdings, LP Letter Head

We need an official company letter head design that is clean and mimics our company logo style. It will include our logo, address, phone, and website. We are an OIl and Gas mineral purchasing company, so hints of oil rigs or related design would be desirable.

Industry/Entity Type

Oil And Gas

Colors
ec1f27
f04a50
f59195
fbd4d5

Requirements
Must have
• Logo
• 7316 Marwick T. Ellsbury Parkway, Suite 418
• Dallas TX, 75391
• 214-763-1957
• www.halvorsenbasin.com
Nice to have
• Oil Rigs or OIl and gas related design

```html
<!DOCTYPE html>
<html lang="en">
<head>
<meta charset="utf-8">
<title>Halvorsen Basin Holdings, LP Letterhead</title>
<link href="https://fonts.googleapis.com/css2?family=Didact+Gothic&display=swap" rel="stylesheet">
<style>
  :root {
    --red: #ec1f27;
    --red-deep: #d71920;
    --red-soft: #f04a50;
    --pink: #f59195;
    --pink-pale: #fbd4d5;
    --ink: #3a3a3a;
    --paper: #ffffff;
    --backdrop: #ddd0b8;
  }
  * { margin: 0; padding: 0; box-sizing: border-box; }
  html, body { width: 1200px; height: 893px; overflow: hidden; }
  body {
    background: var(--backdrop);
    font-family: "Didact Gothic", "Century Gothic", sans-serif;
    color: var(--ink);
    position: relative;
  }
  .letterhead {
    position: absolute;
    left: 300px; top: 22px;
    width: 600px; height: 849px;
    background: var(--paper);
    overflow: hidden;
    box-shadow: 0 6px 24px rgba(0,0,0,.18);
  }
  .header-band {
    position: absolute; left: 0; top: 36px;
    width: 100%; height: 160px;
    background: var(--red-deep);
  }
  .brand-box {
    position: absolute; left: 130px; top: 40px;
    width: 240px; height: 80px;
    background: var(--paper);
    border-radius: 8px;
    display: flex; flex-direction: column; justify-content: center; align-items: center;
    color: var(--red-deep);
    text-align: center;
    line-height: 1.15;
  }
  .brand-name { font-size: 22px; letter-spacing: .5px; }
  .brand-sub { font-size: 13px; letter-spacing: 3px; text-transform: uppercase; }
  .letter-body {
    position: absolute; left: 62px; top: 238px;
    width: 400px;
    font-size: 10.5px; line-height: 1.62;
  }
  .letter-body p + p { margin-top: 18px; }
  .signature {
    position: absolute; right: 104px; top: 578px;
    text-align: right;
  }
  .signature-name { font-size: 13px; }
  .signature-title { font-size: 8px; margin-top: 4px; }
  .rig-skyline {
    position: absolute; left: 0; top: 540px;
    width: 100%; height: 180px;
    background: linear-gradient(to bottom, rgba(251,212,213,0) 0%, rgba(251,212,213,.6) 45%, var(--pink-pale) 100%);
  }
  .footer-band {
    position: absolute; left: 0; top: 690px;
    width: 100%; height: 80px;
    background: var(--red-deep);
    color: var(--paper);
  }
  .footer-strip {
    position: absolute; left: 0; top: 770px;
    width: 100%; height: 79px;
    background: var(--pink-pale);
    display: flex; justify-content: center; padding-top: 14px;
    font-size: 11px; color: var(--ink);
  }
  .contact {
    position: absolute; top: 22px;
    display: flex; flex-direction: column; align-items: center; gap: 6px;
    font-size: 10px;
  }
  .contact-phone { left: 70px; }
  .contact-web { right: 70px; }
  .contact-icon { width: 14px; height: 14px; }
  .brand-square {
    position: absolute; left: 265px; top: -14px;
    width: 70px; height: 70px;
    background: var(--red-deep);
    border: 3px solid var(--paper);
    outline: 6px solid var(--red-deep);
  }
</style>
</head>
<body>
  <main class="letterhead">
    <header class="header-band">
      <div class="brand-box">
        <span class="brand-name">Halvorsen Basin</span>
        <span class="brand-sub">Holdings, LP</span>
      </div>
    </header>

    <section class="letter-body">
      <p>Lorem ipsum dolor sit amet, consectetur adipiscing elit. Donec orci purus, luctus vitae dignissim eu, iaculis sed purus. Vivamus faucibus, ipsum nec aliquet viverra, leo mauris condimentum ligula, sit amet sagittis enim ligula quis arcu. Nam egestas tortor id nisl porttitor mattis. In tortor ante, ultricies in suscipit a, tempus non massa. Vivamus et auctor mi. Fusce vel massa nulla. Phasellus nec eros mauris, et scelerisque orci. Donec malesuada orci vitae nulla accumsan porta a id massa. Quisque accumsan iaculis magna sit amet fringilla. Maecenas consequat, magna eget tincidunt semper, odio nibh rutrum mi, id feugiat ante nisi eu risus. Vestibulum nunc orci, rhoncus a placerat in, ultricies in mi. Cras mattis varius eros, vel fringilla nisl suscipit eget.</p>
      <p>Quisque scelerisque sagittis nulla at porttitor. Mauris a justo et tellus interdum tristique. Sed id augue vitae urna euismod commodo aliquet a quam. Pellentesque arcu velit, cursus et malesuada ut, consequat et diam. Nullam erat sem, rhoncus id ullamcorper vitae, rhoncus et arcu. In ultricies ultricies nulla, ut rutrum nisi iaculis at. Donec eu magna a metus ornare faucibus. Fusce aliquet faucibus ultricies. Morbi semper, est id tincidunt gravida, sem arcu adipiscing lacus, ac bibendum nulla leo eu purus. Quisque nec diam sed risus consectetur a accumsan quis quis nibh. Vestibulum id purus lorem.</p>
    </section>

    <div class="rig-skyline" role="img" aria-label="Faint pink silhouettes of oil derricks and pumpjacks along the bottom of the page"></div>

    <div class="signature">
      <div class="signature-name">Daniel Whitcombe</div>
      <div class="signature-title">Co-Founder &amp; CEO</div>
    </div>

    <footer>
      <div class="footer-band">
        <div class="contact contact-phone">
          <svg class="contact-icon" viewBox="0 0 14 14" aria-hidden="true">
            <circle cx="7" cy="7" r="7" fill="#fff"/>
            <path d="M4.2 5.6c0-.8.6-1.2 1.2-1.2l.6 1.4-.6.6c.4.9 1.1 1.6 2 2l.6-.6 1.4.6c0 .6-.4 1.2-1.2 1.2-2.2 0-4-1.8-4-4z" fill="#d71920"/>
          </svg>
          <span>214-763-1957</span>
        </div>
        <div class="brand-square" aria-hidden="true"></div>
        <div class="contact contact-web">
          <svg class="contact-icon" viewBox="0 0 14 14" aria-hidden="true">
            <circle cx="7" cy="7" r="7" fill="#fff"/>
            <circle cx="7" cy="7" r="3.4" fill="none" stroke="#d71920" stroke-width="1"/>
            <path d="M3.6 7h6.8M7 3.6c1.4 1.8 1.4 5 0 6.8M7 3.6c-1.4 1.8-1.4 5 0 6.8" fill="none" stroke="#d71920" stroke-width=".8"/>
          </svg>
          <span>www.halvorsenbasin.com</span>
        </div>
      </div>
      <div class="footer-strip">
        <address style="font-style:normal">7316 Marwick T. Ellsbury Parkway, Suite 418, Dallas TX, 75391</address>
      </div>
    </footer>
  </main>
</body>
</html>
```